pharmacy/travel clinic business card design

We need a business card for our new business called Brenwick Travel Clinic and Pharmacy. Our primary focus is doing consultations for people before travelling internationally and providing vaccinations and prescriptions for them. While the business is considered a pharmacy, it has more the look and feel of a doctor's office. The design should communicate a professional and trustworthy feel. I have attached a copy of the logo we are going to be using.
Updates
Thanks for the submissions.  If you haven`t been eliminated you are one of the finalists.  Decision will likely be made tomorrow.

Target Market(s)
Customers, other health care professionals, travel agents
Industry/Entity Type
Clinic
Look and feel
Each slider illustrates characteristics of the customer's brand and the style your logo design should communicate.

```html
<!DOCTYPE html>
<html lang="en">
<head>
<meta charset="utf-8">
<title>Brenwick Travel Clinic and Pharmacy – Business Card</title>
<link rel="stylesheet" href="https://fonts.googleapis.com/css2?family=Open+Sans:ital,wght@0,400;0,600;1,400;1,600&display=swap">
<style>
  :root {
    --brand-blue: #1a8fd6;
    --text-gray: #7b7b7b;
    --line-gray: #9a9a9a;
    --bg-light: #fbfbfb;
    --bg-mid: #ececec;
    --bg-low: #dedede;
    --tab-url: #eaf6fd;
    --art-gray: #e2e2e2;
    --art-blue: #4aa8e0;
  }
  * { margin: 0; padding: 0; box-sizing: border-box; }
  html, body { width: 1200px; height: 686px; overflow: hidden; background: #ffffff; }
  .card {
    position: relative;
    width: 1200px;
    height: 686px;
    overflow: hidden;
    font-family: "Open Sans", sans-serif;
    background: linear-gradient(180deg, var(--bg-light) 0%, var(--bg-mid) 55%, var(--bg-low) 100%);
  }
  .tiles { position: absolute; top: 0; right: 0; width: 395px; height: 300px; }
  .side-tab { position: absolute; left: 0; top: 131px; width: 36px; height: 423px; }
  .side-tab__url {
    position: absolute;
    left: 30px; top: 198px;
    transform-origin: 0 0;
    transform: rotate(90deg);
    font-style: italic;
    font-size: 25px;
    line-height: 28px;
    color: var(--tab-url);
    white-space: nowrap;
  }
  .clinic-name {
    position: absolute;
    left: 103px; top: 84px;
    font-style: italic;
    font-weight: 400;
    font-size: 39px;
    line-height: 60px;
    color: var(--brand-blue);
  }
  .clinic-name__line2 { display: block; padding-left: 236px; }
  .product-art {
    position: absolute;
    left: 103px; top: 254px;
    width: 440px; height: 215px;
    border-radius: 6px;
    background: linear-gradient(90deg, var(--art-gray) 0%, var(--art-gray) 45%, var(--art-blue) 55%, var(--art-blue) 100%);
    opacity: 0.85;
  }
  .connector {
    position: absolute;
    left: 543px; top: 333px;
    width: 300px; height: 4px;
    background: linear-gradient(90deg, var(--line-gray), rgba(160,160,160,0.15));
  }
  .person-name {
    position: absolute;
    left: 657px; top: 245px;
    font-size: 90px;
    line-height: 108px;
    letter-spacing: -1px;
    color: var(--text-gray);
    white-space: nowrap;
  }
  .person-name__first { color: var(--brand-blue); }
  .person-email {
    position: absolute;
    right: 105px; top: 332px;
    font-style: italic;
    font-size: 36px;
    line-height: 46px;
    color: var(--text-gray);
  }
  .contact-row {
    position: absolute;
    left: 0; top: 558px;
    width: 1200px; height: 57px;
    font-style: italic;
    white-space: nowrap;
  }
  .contact-row span { position: absolute; top: 0; line-height: 57px; }
  .contact-label { font-size: 35px; color: var(--text-gray); }
  .contact-dot { font-size: 22px; color: var(--text-gray); }
  .contact-value { font-size: 34px; color: var(--brand-blue); letter-spacing: 0.3px; }
  .contact-value--street { font-size: 30px; letter-spacing: 0; }
  .contact-row .divider {
    width: 1px; height: 57px;
    background: var(--line-gray);
  }
</style>
</head>
<body>
<main class="card">
  <svg class="tiles" viewBox="0 0 395 300" aria-hidden="true">
    <defs>
      <linearGradient id="tileFade" x1="1" y1="0" x2="0" y2="1">
        <stop offset="0" stop-color="#c6dbea" stop-opacity="0.9"/>
        <stop offset="1" stop-color="#e4ecf2" stop-opacity="0.2"/>
      </linearGradient>
    </defs>
    <rect x="0" y="0" width="395" height="222" fill="url(#tileFade)" opacity="0.55"/>
    <rect x="135" y="0" width="127" height="90" fill="#dce8f1" opacity="0.8"/>
    <rect x="268" y="0" width="127" height="90" fill="#cfe0ec" opacity="0.9"/>
    <rect x="135" y="92" width="127" height="130" fill="#dfe9f1" opacity="0.8"/>
    <rect x="268" y="92" width="127" height="130" fill="#d6e4ee"/>
    <rect x="135" y="224" width="127" height="76" fill="#e7edf2" opacity="0.6"/>
  </svg>

  <svg class="side-tab" viewBox="0 0 36 423" aria-hidden="true">
    <defs>
      <linearGradient id="tabFill" x1="0" y1="0" x2="1" y2="0">
        <stop offset="0" stop-color="#0a78c4"/>
        <stop offset="1" stop-color="#6ec2ee"/>
      </linearGradient>
    </defs>
    <path d="M0 0 L36 44 L36 379 L0 423 Z" fill="url(#tabFill)"/>
  </svg>
  <div class="side-tab__url">www.yourwebsite.com</div>

  <h1 class="clinic-name">Brenwick Travel Clinic<span class="clinic-name__line2">and Pharmacy</span></h1>

  <div class="product-art" role="img" aria-label="Illustration area: grey and blue medicine capsule with an airplane taking off"></div>
  <div class="connector" aria-hidden="true"></div>

  <p class="person-name"><span class="person-name__first">Your</span>Name</p>
  <p class="person-email">your@email.com</p>

  <section class="contact-row">
    <span class="contact-label" style="left:49px">Phone</span>
    <span class="contact-dot" style="left:157px">•</span>
    <span class="contact-value" style="left:188px">xxx-xxx-xxxx</span>
    <span class="divider" style="left:422px"></span>
    <span class="contact-label" style="left:453px">Fax</span>
    <span class="contact-dot" style="left:517px">•</span>
    <span class="contact-value" style="left:546px">xxx-xxx-xxxx</span>
    <span class="divider" style="left:783px"></span>
    <span class="contact-label" style="left:812px">Street</span>
    <span class="contact-dot" style="left:922px">•</span>
    <span class="contact-value contact-value--street" style="left:950px">Your street here</span>
  </section>
</main>
</body>
</html>
```